Soziale Betreuung für Senioren, die von Herzen kommt!
Zielgruppe
Betreuung von Senioren (keine Pflege) mit den 3 Schwerpunkten „Miteinander reden“, „im Alltag unterstützen“ und „Freizeit gestalten“
Aufgabenstellung
Entwicklung eines Flyers als Hauptwerbemedium, das Interesse bei den Senioren weckt (große
Buchstaben für den Teil, der sich an die Senioren richtet) und auch die Angehörigen überzeugt.
DIN A4 Lang 6-seitig Wickelfalz.

```html
<!DOCTYPE html>
<html lang="de">
<head>
<meta charset="utf-8">
<title>Soziale Betreuung für Senioren – Flyer</title>
<link href="https://fonts.googleapis.com/css2?family=Noto+Serif:ital,wght@0,400;0,700;1,400;1,700&family=Kalam&display=swap" rel="stylesheet">
<style>
:root{
  --navy:#27348b;
  --ink:#1f1f1f;
  --paper:#ffffff;
  --sky-light:#e6f4fa;
  --sky-mid:#c4e5f2;
  --band-dark:#23408f;
  --band-light:#2aa7d8;
}
*{margin:0;padding:0;box-sizing:border-box}
html,body{width:848px;height:1200px;overflow:hidden}
body{background:linear-gradient(#f1f1f1,#e3e3e3);font-family:"Noto Serif",Georgia,serif;color:var(--ink);position:relative}
.sheet{position:absolute;left:31px;width:784px;height:556px;background:var(--paper);box-shadow:0 1px 4px rgba(0,0,0,.25);overflow:hidden}
.sheet.outer{top:29px}
.sheet.inner{top:612px}
.band{position:absolute;left:0;right:0;height:12px;background:linear-gradient(90deg,var(--band-dark),var(--band-light) 60%,var(--band-dark));}
.band::after{content:"";position:absolute;left:0;right:0;bottom:0;height:4px;background:var(--band-light)}
.band.top{top:0}
.band.bottom{bottom:0;transform:scaleY(-1)}
.col{position:absolute;top:12px;bottom:12px;overflow:hidden}
.c1{left:0;width:257px}
.c2{left:257px;width:264px;background:var(--sky-light)}
.c3{left:521px;width:263px}
h2{color:var(--navy);font-weight:700;font-size:12.8px;line-height:1.3}
p{font-size:9.4px;line-height:1.38;text-align:justify;hyphens:auto;-webkit-hyphens:auto}
.pad{padding:10px 16px 0 18px}
.pad p+p{margin-top:10px}
.photo{position:absolute}
.sig{font-family:"Kalam",cursive;color:var(--navy);font-size:14px;line-height:1.3}
.mark{display:flex;align-items:center;justify-content:center;border-radius:50%;background:#e4e6ec;border:2px solid #c9ccd6;color:var(--navy);font-weight:700;font-size:8px;text-align:center}
.web{position:absolute;left:0;right:0;bottom:0;padding:6px 16px 8px;font-size:11px;line-height:1.3}
.web b{display:block;color:var(--navy)}
.contact{font-size:9.4px;line-height:1.38}
.contact .row{margin-top:12px}
.contact .row span{display:inline-block;width:52px}
.quotes{font-style:italic;font-weight:700;color:var(--navy);font-size:12.5px;line-height:1.7}
.rule{position:absolute;left:0;right:0;height:2px;background:var(--navy)}
.checks{list-style:none;font-size:8.7px;line-height:1.3}
.checks li{position:relative;padding-left:12px;margin-bottom:5px;white-space:nowrap}
.checks li svg{position:absolute;left:0;top:2px}
.big p{font-size:12px;line-height:1.24;text-align:justify}
.big h3{color:var(--navy);font-size:14.5px;font-weight:700;line-height:1.3;border-bottom:1px solid var(--navy);display:inline-block;padding-right:12px;margin-bottom:4px}
.disc{float:right;width:90px;height:90px;border-radius:50%;margin:0 -20px 2px 6px;shape-outside:circle(50%)}
.sub{color:var(--navy);font-weight:700;font-size:9.4px;margin-top:10px}
</style>
</head>
<body>

<section class="sheet outer">
  <div class="band top"></div>

  <div class="col c1">
    <div class="pad">
      <h2>Was das alles kostet!?</h2>
      <p style="margin-top:6px">Auch wenn ich meine Leistungen von Herzen anbiete und mir die gemeinsame Zeit mit Ihnen sehr wichtig ist, kann ich diese leider nicht kostenlos anbieten.</p>
      <p>Ich arbeite allein und ohne administrative Verwaltung oder repräsentative Geschäfts&shy;räume. Diesen Kostenvorteil gebe ich an Sie weiter. Auch der Einsatz meines PKWs erfolgt in aller Regel ohne gesonderte Berechnung.</p>
      <p>Da die Betreuungsangebote aufgrund meiner Zertifizierung gemäß § 45b SGB XI anerkannt sind können in vielen Fällen ganz oder zumindest anteilig Kosten über die Pflegeversicherung oder abgerechnet werden. Sprechen Sie mich gern unverbindlich an.</p>
    </div>
    <div class="photo" role="img" aria-label="Foto: Seniorin umarmt herzlich ein junges Mädchen im Freien" style="left:0;right:0;top:271px;bottom:0;background:linear-gradient(160deg,#f1ede0 0%,#d7c5a8 35%,#c8474a 62%,#7e8b5a 100%)"></div>
  </div>

  <div class="col c2">
    <div class="pad" style="padding-right:18px">
      <h2>Können wir das persönlich besprechen?</h2>
      <p style="margin-top:6px">In meinem Angebot stehen die Senioren im Mittelpunkt. Ich kann Unterstützung nur leisten, wenn wir eine Basis für die gemeinsame Zeit finden.</p>
      <p>Daher führe ich mit jedem Interessenten zunächst ein Kennenlern-Gespräch, kostenlos und unverbindlich. Gern auch unter Beteiligung eines Angehörigen.</p>
      <p>Vereinbaren Sie hierzu bitte einen Termin mit mir. Ich freue mich auf Ihren Anruf unter:</p>
      <div class="contact">
        <div class="row"><span>Festnetz:</span>02301 / 45 18 27</div>
        <div class="row"><span>Handy:</span>0176 / 12 48 93 70</div>
        <div class="row">oder per E-Mail an<br>info@seniorenbetreuung-lindenau.de</div>
        <div class="row"><i>Ich freue mich auf Ihren Anruf</i></div>
      </div>
      <div class="sig" style="margin:8px 0 0 8px">Ihre<br>Marlene Thewald</div>
    </div>
    <div style="position:absolute;left:0;right:0;top:404px;bottom:0;background:var(--sky-mid)">
      <div class="mark" style="position:absolute;left:22px;top:10px;width:64px;height:64px">Lindenau</div>
      <div style="position:absolute;left:106px;top:18px;font-size:9.6px;line-height:1.35">
        <b>Seniorenbetreuung Lindenau</b><br>Marlene Thewald<br>Ahornweg 12a<br>58099 Lindenau
      </div>
      <div class="web">Mehr Informationen auch unter<b>www.seniorenbetreuung-lindenau.de</b></div>
    </div>
  </div>

  <div class="col c3">
    <div class="quotes" style="position:absolute;left:16px;top:8px">„Miteinander reden“<br>„Im Alltag unterstützen“<br>„Freizeit gestalten“</div>
    <div class="mark" style="position:absolute;right:16px;top:10px;width:62px;height:62px">Lindenau</div>
    <div class="rule" style="top:98px"></div>
    <div style="position:absolute;left:0;right:0;top:100px;height:72px;background:var(--sky-mid);padding:6px 14px">
      <div style="font-size:15px;line-height:1.3">Soziale Betreuung für Senioren, die von Herzen kommt!</div>
      <div style="color:var(--navy);font-weight:700;font-size:12px;margin-top:2px">Marlene Thewald</div>
    </div>
    <div class="photo" role="img" aria-label="Foto: junge Hände halten die Hände einer älteren Person" style="left:0;right:0;top:172px;height:183px;background:radial-gradient(ellipse at 60% 55%,#f0c7b0 0%,#e9b99d 35%,#f3e2d6 75%,#f6ece4 100%)"></div>
    <div class="rule" style="top:355px"></div>
    <ul class="checks" style="position:absolute;left:12px;right:6px;top:366px">
      <li><svg width="9" height="8" viewBox="0 0 9 8"><path d="M1 4.5l2.4 2.4L8 1" fill="none" stroke="#27348b" stroke-width="1.8"/></svg>Zertifiziertes Angebot für Senioren &amp; Demenzkranke</li>
      <li><svg width="9" height="8" viewBox="0 0 9 8"><path d="M1 4.5l2.4 2.4L8 1" fill="none" stroke="#27348b" stroke-width="1.8"/></svg>Langjährige Erfahrung</li>
      <li><svg width="9" height="8" viewBox="0 0 9 8"><path d="M1 4.5l2.4 2.4L8 1" fill="none" stroke="#27348b" stroke-width="1.8"/></svg>Keine Vertragsbindung</li>
      <li><svg width="9" height="8" viewBox="0 0 9 8"><path d="M1 4.5l2.4 2.4L8 1" fill="none" stroke="#27348b" stroke-width="1.8"/></svg>Unverbindliches kostenloses Kennenlern-Gespräch</li>
      <li><svg width="9" height="8" viewBox="0 0 9 8"><path d="M1 4.5l2.4 2.4L8 1" fill="none" stroke="#27348b" stroke-width="1.8"/></svg>Mobil durch PKW<br>(für Begleitung zum Arzt oder Einkauf uvm.)</li>
      <li><svg width="9" height="8" viewBox="0 0 9 8"><path d="M1 4.5l2.4 2.4L8 1" fill="none" stroke="#27348b" stroke-width="1.8"/></svg>Auch Nacht-Betreuung möglich</li>
    </ul>
    <div class="web" style="background:var(--sky-light)">Mehr Informationen auch unter<b>www.seniorenbetreuung-lindenau.de</b></div>
  </div>

  <div class="band bottom"></div>
</section>

<section class="sheet inner">
  <div class="band top"></div>

  <div class="col c1">
    <div class="photo" role="img" aria-label="Porträtfoto der Betreuerin mit Brille und gemustertem Schal" style="left:0;right:0;top:0;height:246px;background:linear-gradient(160deg,#cfcfcf 0%,#bdbdbd 45%,#a9b8c8 80%,#7f94aa 100%)"></div>
    <div class="rule" style="top:246px"></div>
    <div class="pad" style="position:absolute;top:250px;left:0;right:0">
      <h2>Mein Angebot für alle Senioren</h2>
      <div style="color:var(--navy);font-size:10.5px">„Was ist eigentlich soziale Betreuung?“</div>
      <p style="margin-top:12px">Lieber Interessent,<br>es freut mich, dass Sie sich die Zeit nehmen für diese Information.</p>
      <p style="margin-top:12px">Meine Dienstleistung ist anders. Es geht um „soziale Betreuung“, die dazu beitragen soll, den Alltag zu strukturieren, zu begleiten und mehr Lebensfreude zu gewinnen.</p>
      <p style="margin-top:12px">Ich, Marlene Thewald, möchte Ihnen In dieser Informationsschrift mehr darüber erzählen.</p>
      <p style="margin-top:12px">Es grüßt Sie herzlich</p>
      <div class="sig" style="margin-top:6px">Ihre Marlene Thewald</div>
    </div>
  </div>

  <div class="col c2 big">
    <div style="padding:6px 13px 0 14px">
      <h3>„Miteinander reden“</h3>
      <div class="disc" role="img" aria-label="Foto: lachende Seniorin im Gespräch" style="background:radial-gradient(circle at 60% 40%,#f2dcc6,#d9b48c 55%,#b8484e)"></div>
      <p>Zeit für gemeinsame Gespräche, ohne Eile, ohne Hektik. Respektvoll, mit Vertrauen und Nächstenliebe. Das ist mein Versprechen an Sie. Gespräche über das, was Sie bewegt, oder einfach gemeinsam über Dinge zu lachen.</p>
      <h3 style="margin-top:8px">„Im Alltag unterstützen“</h3>
      <div class="disc" role="img" aria-label="Foto: helfende Hand auf der Schulter einer Seniorin" style="background:radial-gradient(circle at 45% 40%,#e8d2b0,#cdb69a 55%,#8d8f86)"></div>
      <p>Ich unterstütze Sie gern darin, den Haushalt zu organisieren. Zusammen mit Ihnen. Ein schönes Gefühl, vieles noch selbst zu schaffen. Mit ein wenig Unterstützung: Mehr Mobilität und Sicherheit für Sie! Ich helfe Ihnen gern.</p>
      <h3 style="margin-top:8px">„Freizeit gestalten“</h3>
      <div class="disc" role="img" aria-label="Foto: Seniorenpaar auf einer Parkbank" style="background:radial-gradient(circle at 50% 40%,#b9c89a,#7f9a5c 55%,#4c5f3a)"></div>
      <p>Schönes erleben, in einem nicht alltäglichen Umfeld. Eine Auszeit, um neue Kraft zu finden. Sich auf etwas zu freuen, etwas vorhaben. Wenn Sie es wünschen, auch gern bei Ihnen zu Hause.</p>
    </div>
  </div>

  <div class="col c3">
    <div class="pad" style="padding-right:16px">
      <h2 style="white-space:nowrap;font-size:12.6px">Mein Angebot für die Angehörigen</h2>
      <p style="margin-top:6px">Ich möchte Sie gern überzeugen, dass meine Hilfe von Senioren dankbar angenommen wird und auch für Sie einen Mehrwert darstellt.</p>
      <div class="sub">„Weniger Stress für alle“</div>
      <p style="margin-top:0">Als Angehöriger ist man oft vor besondere Herausforderungen gestellt: Schon ein plötzlich notwendiger Arztbesuch der eigenen Eltern/Großeltern bringt den Zeitplan ins Wanken.<br>Ich komme mit meinem PKW und begleite die Senioren zum Arzt, auf Wunsch bis ins Behandlungszimmer.</p>
      <div class="sub">„Mehr gemeinsame Zeit für schöne Dinge“</div>
      <p style="margin-top:0">In der täglichen Routine gerät man leicht in Streit. Während man selbst unter permanenten Zeitdruck leidet, haben die Senioren häufig ein anderes Zeitempfinden.<br>Gewinnen Sie mehr Zeit für die schönen Dinge miteinander.</p>
      <div class="sub">„Unterstützung durch weitere Bezugsperson“</div>
      <p style="margin-top:0">Wie empfinden die Senioren die Unterstützung eines Dritten? Der neue Kontakt mit weiteren Bezugspersonen wird sehr häufig als Bereicherung empfunden.<br>Sofern ein Angehöriger an Demenz erkrankt oder erkrankt ist, ist professionelle Hilfe, Unterstützung und Beratung gefragt. Ich unterstütze gern.<br>Ich bin zertifizierte Demenzbegleiterin. Sie können sich also darauf verlassen, dass Ihre Eltern oder Großeltern in guter Betreuung sind.</p>
    </div>
  </div>

  <div class="band bottom"></div>
</section>

</body>
</html>
```